Website transfer and revamp for consultancy

We are a professional management consultancy and need our current website transferred and modernised from Wix to WordPress with the most efficient SEO updates and blog included. We are open for options of new site set up.

Website must be relatively easy for us to maintain and update ourselves.

Website must also be desktop/mobile/ipad friendly.

www.tellvane-advisory.com

Target Market(s)

General manufacturers, construction, developers, oil and gas

Industry/Entity Type

Management Consulting

Font styles to use
Serif

Colors

Designer to choose colors to be used in the design.

Requirements
Must have
• Must have same bulk content as the existing website as a minimum with the addition of a blog page. We are open to added content.
Nice to have
• Open to designer additions such as "projects completed" and "value created" number generators
Should not have
• DO NOT USE stock photos which are not free for use to use.

```html
<!DOCTYPE html>
<html lang="en">
<head>
<meta charset="utf-8">
<title>Tellvane Advisory – Blog</title>
<link rel="stylesheet" href="https://fonts.googleapis.com/css2?family=Cinzel:wght@400;700&family=Open+Sans:wght@400;600;700&display=swap">
<style>
:root{
  --navy:#1d3a5c;
  --red:#c4202b;
  --ink:#222;
  --muted:#777;
  --line:#d8d8d8;
  --white:#fff;
}
*{margin:0;padding:0;box-sizing:border-box}
html,body{width:881px;height:1200px;overflow:hidden;background:var(--white)}
body{font-family:"Open Sans",Arial,sans-serif;color:var(--ink);position:relative}

.site-header{position:absolute;left:0;top:0;width:881px;height:96px}
.brand{position:absolute;left:72px;top:36px;display:flex;align-items:center;gap:8px}
.brand-dot{width:16px;height:16px;border-radius:50%;background:var(--navy)}
.brand-name{font-family:"Cinzel",Georgia,serif;font-weight:700;color:var(--navy);font-size:15px;line-height:1}
.header-btn{position:absolute;top:18px;height:30px;border-radius:15px;color:var(--white);font-size:11px;font-weight:600;display:flex;align-items:center;justify-content:center}
.btn-consult{left:539px;width:162px;background:var(--navy)}
.btn-brochure{left:706px;width:102px;background:var(--red)}
.main-nav{position:absolute;top:69px;left:264px;font-family:"Cinzel",Georgia,serif;font-size:10px;color:var(--ink)}
.main-nav span{position:absolute;white-space:nowrap}
.main-nav .active{color:var(--navy)}
.nav-marker{position:absolute;left:667px;top:53px;width:7px;height:7px;border-radius:50%;background:var(--red)}
.search{position:absolute;left:799px;top:70px}

.hero{position:absolute;left:0;top:96px;width:881px;height:234px}
.hero-photo{position:absolute;inset:0;background:linear-gradient(180deg,#2a3f66 0%,#5d5f85 35%,#c97a4e 58%,#3b3c4c 80%,#1e2433 100%)}
.hero-title{position:absolute;left:73px;top:78px;font-family:"Cinzel",Georgia,serif;font-weight:700;font-size:34px;color:var(--white)}
.hero-curve{position:absolute;left:0;bottom:0}

.posts{position:absolute;top:363px;left:72px;width:738px}
.post{position:absolute;top:0;width:238px}
.post-photo{width:238px;height:152px}
.post-title{margin-top:24px;font-size:15px;line-height:20px;color:var(--ink);font-weight:400}
.post-meta{margin-top:7px;font-size:10px;color:var(--muted);display:flex;align-items:center;gap:5px}
.post-excerpt{margin-top:8px;font-size:9.6px;line-height:18px;color:#555;height:36px;overflow:hidden}
.read-more{display:block;margin-top:10px;font-size:11px;font-weight:700;color:var(--red)}

.stats{position:absolute;left:0;top:736px;width:881px;height:194px;background:linear-gradient(100deg,#2c2d3a 0%,#5a4a44 28%,#d89a63 55%,#e9a45e 75%,#8c4a1a 100%)}
.stat-ring{position:absolute;top:42px;width:111px;height:111px;border:2px solid var(--white);border-radius:50%;display:flex;align-items:center;justify-content:center}
.stat-num{position:absolute;top:60px;font-size:34px;font-weight:700;color:var(--white)}
.stat-label{position:absolute;top:108px;font-family:"Cinzel",Georgia,serif;font-size:17px;color:var(--white)}

.site-footer{position:absolute;left:0;top:930px;width:881px;height:270px}
.footer-brand{position:absolute;left:72px;top:104px;display:flex;align-items:center;gap:8px}
.footer-brand-dot{width:22px;height:22px;border-radius:50%;background:var(--navy)}
.footer-brand-name{font-family:"Cinzel",Georgia,serif;font-weight:700;font-size:17px;color:var(--navy);white-space:nowrap}
.footer-heading{position:absolute;top:58px;font-family:"Cinzel",Georgia,serif;font-weight:400;font-size:15px;color:var(--ink);white-space:nowrap}
.quick-links{position:absolute;left:294px;top:92px;list-style:none;font-size:9px;color:#555;line-height:18.3px}
.news-text{position:absolute;left:419px;top:92px;font-size:9px;color:#555;line-height:15px;width:170px}
.email-field{position:absolute;left:419px;top:134px;width:186px;height:22px;border-bottom:1px solid var(--line);font-size:9px;color:#999;padding:5px 10px}
.subscribe{position:absolute;left:421px;top:169px;width:77px;height:24px;border-radius:12px;background:var(--red);color:var(--white);font-size:8.6px;font-weight:600;display:flex;align-items:center;justify-content:center}
.contact-row{position:absolute;left:642px;font-size:9px;color:#555;line-height:13.5px;display:flex;gap:14px}
.contact-row svg{flex:none;margin-top:1px}
.footer-rule{position:absolute;left:72px;top:216px;width:737px;height:1px;background:var(--line)}
.copyright{position:absolute;left:72px;top:238px;font-size:9px;color:#555}
.social{position:absolute;top:234px;width:19px;height:19px;border:1px solid var(--red);border-radius:50%}
</style>
</head>
<body>

<header class="site-header">
  <div class="brand"><span class="brand-dot"></span><span class="brand-name">Tellvane Advisory</span></div>
  <div class="header-btn btn-consult">ARRANGE A CONSULTATION</div>
  <div class="header-btn btn-brochure">BROCHURE</div>
  <span class="nav-marker"></span>
  <nav class="main-nav">
    <span style="left:0">HOME</span>
    <span style="left:55px">ABOUT US</span>
    <span style="left:129px">CONFLICT ADVISORY</span>
    <span style="left:259px">CONTRACT ADVISORY</span>
    <span class="active" style="left:393px">BLOG</span>
    <span style="left:445px">CONTACT US</span>
  </nav>
  <svg class="search" width="10" height="10" viewBox="0 0 10 10"><circle cx="4" cy="4" r="3" fill="none" stroke="#222" stroke-width="1.6"/><line x1="6.2" y1="6.2" x2="9.2" y2="9.2" stroke="#222" stroke-width="1.8"/></svg>
</header>

<section class="hero">
  <div class="hero-photo" role="img" aria-label="City skyline with glass towers at sunset"></div>
  <h1 class="hero-title">BLOG</h1>
  <svg class="hero-curve" width="881" height="70" viewBox="0 0 881 70">
    <path d="M0 70 Q440 -35 881 65 L881 70 Z" fill="#fff"/>
    <path d="M0 68 Q440 -35 881 62" fill="none" stroke="#1d3a5c" stroke-width="3"/>
  </svg>
</section>

<section class="posts">
  <article class="post" style="left:0">
    <div class="post-photo" role="img" aria-label="Business people talking by an office window" style="background:linear-gradient(160deg,#e6e9ee,#8d96a3 60%,#c9607a)"></div>
    <h2 class="post-title">The Crying Need for Effective Contract Management</h2>
    <div class="post-meta"><svg width="9" height="9" viewBox="0 0 9 9"><rect x=".5" y="1.5" width="8" height="7" fill="none" stroke="#1d3a5c"/><rect x=".5" y="1.5" width="8" height="2" fill="#1d3a5c"/></svg>28/02/2016 &nbsp;| <svg width="9" height="9" viewBox="0 0 9 9"><circle cx="4.5" cy="2.5" r="2.2" fill="#1d3a5c"/><path d="M0.5 9 Q4.5 3 8.5 9Z" fill="#1d3a5c"/></svg>Aidan</div>
    <p class="post-excerpt">With the collapse of commodity prices in recent times, increasingly, companies stemming from the</p>
    <a class="read-more">READ MORE</a>
  </article>
  <article class="post" style="left:250px">
    <div class="post-photo" role="img" aria-label="Hands signing a contract document" style="background:linear-gradient(150deg,#f4f1ec,#d9d4cc 55%,#9aa2ad)"></div>
    <h2 class="post-title">Negotiation – Looking beyond the problem....</h2>
    <div class="post-meta"><svg width="9" height="9" viewBox="0 0 9 9"><rect x=".5" y="1.5" width="8" height="7" fill="none" stroke="#1d3a5c"/><rect x=".5" y="1.5" width="8" height="2" fill="#1d3a5c"/></svg>28/02/2016 &nbsp;| <svg width="9" height="9" viewBox="0 0 9 9"><circle cx="4.5" cy="2.5" r="2.2" fill="#1d3a5c"/><path d="M0.5 9 Q4.5 3 8.5 9Z" fill="#1d3a5c"/></svg>Aidan</div>
    <p class="post-excerpt">With the increase of cross border and cross continent business transactions comes the increased</p>
    <a class="read-more">READ MORE</a>
  </article>
  <article class="post" style="left:499px">
    <div class="post-photo" role="img" aria-label="Three people in a mediation meeting at a table" style="background:linear-gradient(160deg,#d8d2bf,#e8e4dc 45%,#c9552e 60%,#b8bcc6)"></div>
    <h2 class="post-title">There's No Me in Mediation - Neutrality</h2>
    <div class="post-meta"><svg width="9" height="9" viewBox="0 0 9 9"><rect x=".5" y="1.5" width="8" height="7" fill="none" stroke="#1d3a5c"/><rect x=".5" y="1.5" width="8" height="2" fill="#1d3a5c"/></svg>28/02/2016 &nbsp;| <svg width="9" height="9" viewBox="0 0 9 9"><circle cx="4.5" cy="2.5" r="2.2" fill="#1d3a5c"/><path d="M0.5 9 Q4.5 3 8.5 9Z" fill="#1d3a5c"/></svg>Aidan</div>
    <p class="post-excerpt">The process of mediation, may be defined as a voluntary, non-binding and private dispute resolution</p>
    <a class="read-more">READ MORE</a>
  </article>
</section>

<section class="stats" role="img" aria-label="Handshake between two business people">
  <div class="stat-ring" style="left:72px">
    <svg width="46" height="46" viewBox="0 0 46 46" fill="#fff">
      <g><rect x="15.5" y="10" width="5" height="24"/><rect x="6" y="19.5" width="24" height="5"/><rect x="15.5" y="10" width="5" height="24" transform="rotate(45 18 22)"/><rect x="15.5" y="10" width="5" height="24" transform="rotate(-45 18 22)"/></g>
      <circle cx="18" cy="22" r="9"/>
      <circle cx="18" cy="22" r="3.5" fill="#6a5448"/>
      <circle cx="35" cy="13" r="5"/><circle cx="35" cy="13" r="2" fill="#6a5448"/>
      <circle cx="35" cy="33" r="5"/><circle cx="35" cy="33" r="2" fill="#6a5448"/>
    </svg>
  </div>
  <div class="stat-num" style="left:206px">125830</div>
  <div class="stat-label" style="left:209px">PROJECTS COMPLETED</div>
  <div class="stat-ring" style="left:487px">
    <svg width="42" height="42" viewBox="0 0 42 42"><circle cx="21" cy="21" r="20" fill="#fff"/><path d="M12 21 L19 28 L31 15" fill="none" stroke="#d2894e" stroke-width="5"/></svg>
  </div>
  <div class="stat-num" style="left:620px">125830</div>
  <div class="stat-label" style="left:624px">VALUE CREATED</div>
</section>

<footer class="site-footer">
  <div class="footer-brand"><span class="footer-brand-dot"></span><span class="footer-brand-name">Tellvane Advisory</span></div>

  <h3 class="footer-heading" style="left:294px">Quick Links</h3>
  <ul class="quick-links">
    <li>Home</li><li>About Us</li><li>Conflict Advisory</li><li>Contract Advisory</li><li>Blog</li><li>Contact Us</li>
  </ul>

  <h3 class="footer-heading" style="left:419px">Newsletter Subscription</h3>
  <p class="news-text">Register your Email Address to get Information about us</p>
  <div class="email-field">Email Address</div>
  <div class="subscribe">SUBSCRIBE</div>

  <h3 class="footer-heading" style="left:642px">Contact Us</h3>
  <div class="contact-row" style="top:100px">
    <svg width="8" height="11" viewBox="0 0 8 11"><path d="M4 11 L0.7 5.5 A3.6 3.6 0 1 1 7.3 5.5Z" fill="#c4202b"/><circle cx="4" cy="4" r="1.3" fill="#fff"/></svg>
    <span>Tellvane Ltd, 2nd Floor,<br>Mercer House, 8-10 Quay Lane,<br>Harbour Quarter, Lisburn, LN4 2QT</span>
  </div>
  <div class="contact-row" style="top:153px">
    <svg width="9" height="9" viewBox="0 0 9 9"><path d="M1 0.5 L3 0.5 L3.8 2.8 L2.6 3.7 Q3.6 5.6 5.3 6.4 L6.2 5.2 L8.5 6 L8.5 8 Q4 9 0.5 3Z" fill="#c4202b"/></svg>
    <span>1 555 010 0199</span>
  </div>
  <div class="contact-row" style="top:180px">
    <svg width="10" height="8" viewBox="0 0 10 8"><rect width="10" height="8" fill="#c4202b"/><path d="M0 0.5 L5 4.5 L10 0.5" fill="none" stroke="#fff" stroke-width="1"/></svg>
    <span>mhale@tellvane-advisory.com</span>
  </div>

  <div class="footer-rule"></div>
  <p class="copyright">Copyrights © 2018, Tellvane-advisory. All rights reserved.</p>
  <span class="social" style="left:717px"></span>
  <span class="social" style="left:741px"></span>
  <span class="social" style="left:765px"></span>
  <span class="social" style="left:789px"></span>
</footer>

</body>
</html>
```